Online Guide to Events for Adults in Pennsylvania

8GrownupsHub is an online event advertisement business for local companies throughout the state to feature their events, music festivals, restaurant, bed & breakfast promotions, wineries and vineyards, theatre and entertainment. The business is geared towards adults. The homepage shall be sleek and elegant, yet user friendly and events searchable on from the homepage. The homepage shall also have an area for local event advertisement spots that rotate every few seconds. Color scheme should include a deep or wine red and some black.

I have attached the current logo and a couple of photos for use. Feel free to use any photos you have available as an example.

A few examples of websites that are similar to what I am looking for:

http://orchardcellarguide.example/

http://www.roamtimberfield.example/index.asp

I also enjoy the design of many of the websites built by townforge.example.

Target Market(s)

Adults, ages 18 - 65

Industry/Entity Type

Advertising

Number of Pages Required

2 page

Font styles to use
Decorative
Script

Requirements
Must have
• Searchable field on homepage whether it is in the form of a state map with counties, or search by zip code, county, event type and month.
Should not have
• Nothing that appears cartoon like.

```html
<!DOCTYPE html>
<html lang="en">
<head>
<meta charset="utf-8">
<title>8GrownupsHub – Your Cultural Day Out In Pennsylvania</title>
<link href="https://fonts.googleapis.com/css2?family=Roboto:wght@300;400;500;700&family=Roboto+Condensed:wght@300;400;700&display=swap" rel="stylesheet">
<style>
:root{
  --wine:#cf161c;
  --wine-dark:#a51015;
  --ink:#222222;
  --text:#555555;
  --muted:#8a8a8a;
  --line:#d8d8d8;
  --paper:#ffffff;
  --mist:#ececec;
  --slate:#5e5e5e;
  --charcoal:#333333;
  --btn-dark:#555555;
}
*{box-sizing:border-box;margin:0;padding:0}
html,body{width:1200px;height:2169px;overflow:hidden}
body{position:relative;background:var(--paper);font-family:"Roboto",Arial,sans-serif;color:var(--ink)}

/* header */
.site-header{position:absolute;left:0;top:0;width:1200px;height:120px;background:var(--paper);border-bottom:1px solid var(--line)}
.brand{position:absolute;left:140px;top:40px;font-family:"Roboto",sans-serif;font-weight:400;font-size:28px;color:var(--text);letter-spacing:.3px}
.upload-btn{position:absolute;top:16px;height:33px;width:123px;border-radius:4px;background:var(--btn-dark);color:#fff;font-size:12.5px;display:flex;align-items:center;justify-content:center;gap:7px}
.upload-btn .ic{width:14px;height:14px;border:1px solid #ddd;border-radius:50%;display:flex;align-items:center;justify-content:center;font-size:8px;line-height:1}
.lang{position:absolute;left:1011px;top:16px;width:57px;height:33px;border:1px solid #ccc;border-radius:4px;display:flex;align-items:center;justify-content:center;gap:7px;font-size:10px;color:#555}
.lang-chip{width:24px;height:15px;background:#274a9a;border:1px solid #c22}
.main-nav{position:absolute;left:526px;top:68px;width:542px;height:30px;border-bottom:1px solid var(--line)}
.main-nav a{position:absolute;top:0;font-family:"Roboto Condensed",sans-serif;font-size:19px;color:#666;text-decoration:none;white-space:nowrap}
.main-nav a.active{border-bottom:2px solid var(--wine);padding-bottom:5px}

/* hero */
.hero{position:absolute;left:0;top:120px;width:1200px;height:682px;background:linear-gradient(180deg,#3f4b5b 0%,#556172 35%,#4a4a47 65%,#3a3228 100%)}
.hero-title{position:absolute;left:0;top:185px;width:1200px;text-align:center;font-weight:300;font-size:60px;line-height:80px;color:#fff;text-shadow:0 2px 6px rgba(0,0,0,.5)}
.hero-arrow{position:absolute;top:213px}
.search-panel{position:absolute;left:133px;top:505px;width:935px;height:131px;border:1px solid rgba(255,255,255,.35);border-radius:14px;background:rgba(30,30,30,.55)}
.search-badge{position:absolute;left:563px;top:470px;width:74px;height:74px;border-radius:50%;background:#222;border:3px solid rgba(255,255,255,.75)}
.search-badge::after{content:"";position:absolute;left:12px;top:12px;width:44px;height:44px;border-radius:50%;background:#fff}
.search-label{position:absolute;left:29px;top:25px;font-size:16px;font-weight:500;color:#fff;letter-spacing:.2px}
.field{position:absolute;top:61px;height:40px;border:1px solid #fff;border-radius:4px;color:#fff;font-size:16px;font-weight:500;display:flex;align-items:center;padding-left:10px}
.field .caret{position:absolute;right:0;top:0;width:34px;height:38px;border-left:1px solid #fff;display:flex;align-items:center;justify-content:center}
.submit{position:absolute;left:815px;top:61px;width:94px;height:40px;background:#e8141b;color:#fff;font-size:15px;font-weight:700;border-radius:3px;display:flex;align-items:center;justify-content:center}

/* section headings */
.section-title{position:absolute;left:0;width:1200px;text-align:center;font-family:"Roboto Condensed",sans-serif;font-weight:400;font-size:44px;color:var(--ink)}
.section-title em{font-style:normal;color:var(--wine)}
.divider{position:absolute;left:207px;width:786px;height:16px}

/* categories */
.categories{position:absolute;left:0;top:802px;width:1200px;height:376px;background:var(--paper)}
.cat{position:absolute;top:150px;width:165px;height:165px;border-radius:50%;display:flex;align-items:center;justify-content:center;text-align:center;color:#fff;font-family:"Roboto Condensed",sans-serif;font-weight:700;font-size:24px;line-height:30px;text-shadow:0 2px 4px rgba(0,0,0,.6)}

/* highlights */
.highlights{position:absolute;left:0;top:1178px;width:1200px;height:492px;background:var(--mist)}
.card{position:absolute;top:152px;width:283px;height:283px;border:3px solid #fff;box-shadow:0 1px 5px rgba(0,0,0,.25);overflow:hidden}
.card-caption{position:absolute;left:0;bottom:0;width:100%;height:88px;background:rgba(20,20,20,.72);color:#fff;padding:12px 0 0 16px}
.card-caption h3{font-weight:400;font-size:20px;margin-bottom:6px}
.card-caption p{font-size:12.5px;line-height:16px;color:#ddd;width:190px}
.date{position:absolute;right:14px;top:14px;width:56px;height:56px;border-radius:50%;background:var(--wine);text-align:center;color:#fff;padding-top:10px}
.date b{display:block;font-weight:400;font-size:20px;line-height:20px}
.date span{font-size:12px}
.hl-arrow{position:absolute;top:236px}

/* promo tiles */
.tile{position:absolute;top:1713px;width:283px;height:261px;overflow:hidden}
.weather{background:#5f5f5f;color:#fff}
.weather h4{position:absolute;left:27px;top:22px;font-size:23px;font-weight:500}
.weather p{position:absolute;left:27px;top:57px;font-size:14px;color:#e6e6e6}
.weather .temp{position:absolute;left:105px;top:92px;font-size:76px;font-weight:500;line-height:80px}
.weather .unit{position:absolute;left:208px;top:100px;font-size:24px}
.weather .sun{position:absolute;left:39px;top:110px}
.weather .skyline{position:absolute;left:0;bottom:0;width:100%;height:80px;background:linear-gradient(180deg,rgba(80,80,80,0),#4c4c4c)}
.app-tile h4{position:absolute;left:150px;top:78px;width:120px;text-align:center;font-family:"Roboto Condensed",sans-serif;font-weight:700;font-size:30px;line-height:33px;color:#fff}
.resort h4{position:absolute;left:27px;top:24px;font-family:"Roboto Condensed",sans-serif;font-weight:700;font-size:29px;color:#fff;text-shadow:0 1px 3px rgba(0,0,0,.5)}
.resort .sub{position:absolute;left:27px;top:58px;font-family:"Roboto Condensed",sans-serif;font-weight:700;font-size:23px;color:#fff;text-shadow:0 1px 3px rgba(0,0,0,.5)}
.resort .offer{position:absolute;left:31px;top:102px;font-family:"Roboto Condensed",sans-serif;font-weight:700;font-size:27px;color:#fff;text-shadow:0 1px 3px rgba(0,0,0,.5)}
.resort .book{position:absolute;left:31px;top:147px;width:114px;height:33px;background:rgba(40,40,40,.75);color:#fff;font-size:16px;font-weight:700;display:flex;align-items:center;justify-content:center}

/* newsletter + footer */
.newsletter{position:absolute;left:0;top:2024px;width:1200px;height:97px;background:var(--slate)}
.newsletter h5{position:absolute;left:133px;top:26px;font-weight:500;font-size:24px;color:#fff}
.newsletter small{position:absolute;left:134px;top:58px;font-size:10.5px;color:#eee}
.email{position:absolute;left:357px;top:29px;width:253px;height:39px;background:#fff;font-size:13px;color:#333;display:flex;align-items:center;padding-left:14px}
.signup{position:absolute;left:632px;top:29px;width:82px;height:39px;background:var(--wine);color:#fff;font-size:13px;font-weight:700;display:flex;align-items:center;justify-content:center}
.social{position:absolute;top:28px;width:40px;height:40px;border-radius:50%;border:2px solid #fff}
.site-footer{position:absolute;left:0;top:2121px;width:1200px;height:48px;background:var(--charcoal);color:#ddd;font-size:12.5px;display:flex;align-items:center;justify-content:center}
</style>
</head>
<body>

<header class="site-header">
  <div class="brand">8GrownupsHub</div>
  <div class="upload-btn" style="left:739px"><span class="ic">↑</span>Upload Events</div>
  <div class="upload-btn" style="left:875px"><span class="ic">↑</span>Upload Events</div>
  <div class="lang"><span class="lang-chip"></span>⌄</div>
  <nav class="main-nav">
    <a class="active" style="left:0">What are you looking for?</a>
    <a style="left:232px">Where to go?</a>
    <a style="left:366px">PA for?</a>
    <a style="left:453px">Contact Us</a>
  </nav>
</header>

<section class="hero" role="img" aria-label="Evening city skyline of a Pennsylvania downtown with lit towers along the river">
  <h1 class="hero-title">Your Cultural Day Out<br>In Pennsylvania</h1>
  <svg class="hero-arrow" style="left:72px" width="46" height="214" viewBox="0 0 46 214"><polyline points="44,2 3,107 44,212" fill="none" stroke="#fff" stroke-width="3"/></svg>
  <svg class="hero-arrow" style="left:1084px" width="46" height="214" viewBox="0 0 46 214"><polyline points="2,2 43,107 2,212" fill="none" stroke="#fff" stroke-width="3"/></svg>
  <form class="search-panel">
    <div class="search-label">SEARCH IN PENNSYLVANIA</div>
    <div class="field" style="left:28px;width:168px">Zipcode</div>
    <div class="field" style="left:223px;width:168px">County<span class="caret">⌄</span></div>
    <div class="field" style="left:420px;width:169px">Event Type<span class="caret">⌄</span></div>
    <div class="field" style="left:616px;width:170px">Select Month<span class="caret">⌄</span></div>
    <div class="submit">SUBMIT</div>
  </form>
  <div class="search-badge"></div>
</section>

<section class="categories">
  <h2 class="section-title" style="top:40px">What Are You <em>Looking</em> For?</h2>
  <svg class="divider" style="top:100px" viewBox="0 0 786 16"><polyline points="0,8 375,8 393,22 411,8 786,8" fill="none" stroke="#ddd" stroke-width="1.2"/></svg>
  <div class="cat" style="left:132px;background:radial-gradient(circle,#c2334a,#7a0f1e)" role="img" aria-label="Festival crowd in red stage light">Music &amp;<br>Festivals</div>
  <div class="cat" style="left:324px;background:radial-gradient(circle,#d99a3a,#a34a24)" role="img" aria-label="Colourful painted artwork">Arts &amp;<br>Culture</div>
  <div class="cat" style="left:518px;background:radial-gradient(circle,#6f7258,#4a5238);box-shadow:0 0 0 6px #c8cdd4 inset" role="img" aria-label="Historic stone monument in a park">History &amp;<br>Heritage</div>
  <div class="cat" style="left:710px;background:radial-gradient(circle,#a08a6c,#5a4632)" role="img" aria-label="Cosy guest bedroom">Bed &amp;<br>Breakfasts</div>
  <div class="cat" style="left:904px;background:radial-gradient(circle,#b39a82,#5a3a2c)" role="img" aria-label="Couple dining at a restaurant table">Wine &amp;<br>Dine</div>
</section>

<section class="highlights">
  <h2 class="section-title" style="top:32px">Events <em>Highlights</em> In PA</h2>
  <svg class="divider" style="top:88px" viewBox="0 0 786 16"><polyline points="0,8 375,8 393,22 411,8 786,8" fill="none" stroke="#c8c8c8" stroke-width="1.2"/></svg>
  <svg class="hl-arrow" style="left:53px" width="46" height="120" viewBox="0 0 46 120"><polyline points="44,2 3,60 44,118" fill="none" stroke="#aaa" stroke-width="2"/></svg>
  <svg class="hl-arrow" style="left:1101px" width="46" height="120" viewBox="0 0 46 120"><polyline points="2,2 43,60 2,118" fill="none" stroke="#aaa" stroke-width="2"/></svg>

  <article class="card" style="left:133px;background:linear-gradient(180deg,#7fa4c8,#b07a48 60%,#3c3a2e)" role="img" aria-label="City skyline with yellow bridge over the river">
    <div class="card-caption"><h3>Lorem ipsum dolor</h3><p>Lorem ipsum dolor sit amet, con ctetuer adipiscing elit</p><div class="date"><b>11</b><span>June</span></div></div>
  </article>
  <article class="card" style="left:460px;background:linear-gradient(180deg,#8aa6c8,#4f7a6a 45%,#8a6a4a)" role="img" aria-label="Green domed capitol building above town rooftops">
    <div class="card-caption"><h3>Lorem ipsum dolor</h3><p>Lorem ipsum dolor sit amet, con ctetuer adipiscing elit</p><div class="date"><b>11</b><span>June</span></div></div>
  </article>
  <article class="card" style="left:787px;background:linear-gradient(180deg,#0f2446,#3b5a86 50%,#1d4a46)" role="img" aria-label="Illuminated fountain at night">
    <div class="card-caption"><h3>Lorem ipsum dolor</h3><p>Lorem ipsum dolor sit amet, con ctetuer adipiscing elit</p><div class="date"><b>11</b><span>June</span></div></div>
  </article>
</section>

<aside class="tile weather" style="left:133px">
  <h4>PENNSYLVANIA</h4>
  <p>Monday, 1:00pm, mostly clear</p>
  <svg class="sun" width="58" height="58" viewBox="0 0 58 58"><g stroke="#f5b400" stroke-width="3" stroke-linecap="round"><line x1="29" y1="3" x2="29" y2="11"/><line x1="29" y1="47" x2="29" y2="55"/><line x1="3" y1="29" x2="11" y2="29"/><line x1="47" y1="29" x2="55" y2="29"/><line x1="11" y1="11" x2="16" y2="16"/><line x1="42" y1="42" x2="47" y2="47"/><line x1="47" y1="11" x2="42" y2="16"/><line x1="16" y1="42" x2="11" y2="47"/></g><circle cx="29" cy="29" r="12" fill="none" stroke="#f5b400" stroke-width="3"/></svg>
  <div class="temp">26</div><div class="unit">°C</div>
  <div class="skyline" role="img" aria-label="Faint city skyline silhouette"></div>
</aside>

<aside class="tile app-tile" style="left:460px;background:linear-gradient(160deg,#3a2a4a,#5a3a5a 45%,#2a2030)" role="img" aria-label="Smartphone held in front of a city at dusk">
  <h4>FIND<br>YOUR<br>APP</h4>
</aside>

<aside class="tile resort" style="left:787px;background:linear-gradient(180deg,#2e6f78,#3f9aa0 55%,#5a4030)" role="img" aria-label="Resort pool with lounge chairs">
  <h4>COME &amp; ENJOY!</h4>
  <div class="sub">At A Luxurious Resort</div>
  <div class="offer">Get 20% Off</div>
  <div class="book">BOOK NOW</div>
</aside>

<section class="newsletter">
  <h5>Newsletter Sign Up</h5>
  <small>Sign Up! To Get All The Updates And News</small>
  <div class="email">EMAIL ADDRESS</div>
  <div class="signup">SIGN UP</div>
  <span class="social" style="left:866px;background:#3b5c9e"></span>
  <span class="social" style="left:920px;background:#26a6dc"></span>
  <span class="social" style="left:972px;background:#1d7db8"></span>
  <span class="social" style="left:1025px;background:#c9202a"></span>
</section>

<footer class="site-footer">Copyright 2015 8 Grownups Hub. All Rights Reserved.</footer>

</body>
</html>
```